Business Card Design Project

We are looking for an eye catching, unique business card design that incorporates our logo and a photo of the mortgage associate.

We will need to have our business address included (could be on the back of the card), as well as the mortgage associate's information:

Name
Position
Phone
Email

Logo attached.

Target Market(s)

Clients (people purchasing homes, renewing existing mortgages, or refinancing existing mortgages)
Referral sources such as realtors, financial advisors, relocation specialists, real estate lawyers...

Industry/Entity Type

Business

Requirements
Must have
• Logo
Name and contact information of associate
Address of brokerage
Nice to have
• Photo of the agent

```html
<!DOCTYPE html>
<html lang="en">
<head>
<meta charset="utf-8">
<title>Keystone Home Lending – Business Cards</title>
<link rel="stylesheet" href="https://fonts.googleapis.com/css2?family=Open+Sans:wght@400;600;800&display=swap">
<style>
  :root {
    --backdrop: #c9c9c9;
    --card: #f7f7f5;
    --ink: #2b2b2b;
    --ink-soft: #3a3a3a;
    --brand-red: #a8161c;
    --brand-blue: #5b86c5;
    --photo-light: #a9a9a9;
    --photo-dark: #1c1c1e;
  }
  * { box-sizing: border-box; margin: 0; padding: 0; }
  html, body {
    width: 1200px; height: 831px; overflow: hidden;
    background: var(--backdrop);
    font-family: "Open Sans", Arial, sans-serif;
    color: var(--ink);
  }
  .canvas { position: relative; width: 1200px; height: 831px; }

  .card {
    position: absolute;
    width: 580px; height: 330px;
    background: var(--card);
    box-shadow: 0 6px 18px rgba(0,0,0,0.18);
  }
  .card--front { left: 500px; top: 70px; }
  .card--back  { left: 130px; top: 430px; }

  .brand {
    display: flex; align-items: center; gap: 12px;
    font-weight: 800; color: var(--ink);
    text-transform: uppercase; letter-spacing: 0.5px;
    line-height: 1;
  }
  .brand__mark {
    width: 16px; height: 16px; background: var(--brand-red);
  }
  .card--front .brand {
    position: absolute; left: 0; right: 0; top: 112px;
    justify-content: center; font-size: 40px;
  }
  .card--front .brand__mark { width: 26px; height: 26px; }

  .address {
    position: absolute; left: 0; right: 0; top: 212px;
    text-align: center; font-size: 15px; color: var(--ink-soft);
  }
  .address__sep {
    display: inline-block; width: 5px; height: 5px; margin: 0 6px 3px;
    background: var(--brand-blue); vertical-align: middle;
  }

  .card--back .brand {
    position: absolute; left: 60px; top: 60px; font-size: 22px;
  }
  .contact {
    position: absolute; left: 120px; top: 145px;
    font-size: 16px; line-height: 1.3; color: var(--ink-soft);
  }
  .contact__name { font-weight: 600; font-size: 17px; color: var(--ink); }
  .contact__email { font-size: 13px; margin-top: 2px; }
  .contact__rule {
    margin-top: 4px; width: 190px; height: 4px;
    background: repeating-linear-gradient(90deg, var(--brand-blue) 0 4px, transparent 4px 6px);
  }

  .portrait {
    position: absolute; left: 385px; top: 120px;
    width: 165px; height: 180px;
    background: linear-gradient(180deg, var(--photo-light) 0%, #8e8e8e 55%, var(--photo-dark) 100%);
  }
</style>
</head>
<body>
  <main class="canvas">
    <section class="card card--front">
      <div class="brand"><span class="brand__mark"></span>Keystone Home Lending</div>
      <p class="address">11222<span class="address__sep"></span>Address of Brokerage<span class="address__sep"></span>Comes here<span class="address__sep"></span>Solutionland</p>
    </section>

    <section class="card card--back">
      <div class="brand"><span class="brand__mark"></span>Keystone Home Lending</div>
      <div class="contact">
        <p class="contact__name">Daniel Whitmore</p>
        <p class="contact__role">account manager</p>
        <p class="contact__phone">00 4412 7788</p>
        <p class="contact__email">danielwhitmore@keystonehome.com</p>
        <div class="contact__rule"></div>
      </div>
      <div class="portrait" role="img" aria-label="Portrait photo of the account manager in a dark suit"></div>
    </section>
  </main>
</body>
</html>
```